New Business Card for Web Design/Internet Marketing Company

Looking for a great looking new business card. We are a 10 year old web design, internet marketing and website management company that works mostly with small businesses.

Our new card needs to better match the colors and style of our website, be bold, extremely usable and slightly edgy.

Target Market(s)

Small/Medium businesses that have websites

Industry/Entity Type

Internet

Requirements
Must have
• Front and back design, full color, rounded corners please

Must use the colors/style of our website (JPG provided)

INFO FOR CARDS (as readable as possible please)
Mark Tilden
President/CEO
mark@brivatnet.example
Phone: 520-318-7051
Toll Free: 866-318-7051
Address: 4125 W. Larkspur Ave. Ste. 160, Tucson, AZ 85799

THINGS I WANT TO PROMOTE (if there is room):
1. Our Website - www.brivatnet.example

2. Social Media
Twitter: @brivatnet
Facebook: www.facebook.com/brivatnet

3. Our Services
Web Design
Internet Marketing
Website Management

```html
<!DOCTYPE html>
<html lang="en">
<head>
<meta charset="utf-8">
<title>Brivatnet Business Card</title>
<link rel="stylesheet" href="https://fonts.googleapis.com/css2?family=Ubuntu:wght@400;500;700&family=Open+Sans:ital,wght@0,400;0,600;1,400&display=swap">
<style>
  :root {
    --navy: #1f2f86;
    --navy-deep: #141f5e;
    --navy-light: #2e45b0;
    --orange: #f07c1e;
    --ink: #2a2a2a;
    --paper: #ffffff;
    --backdrop: #e6e6e8;
  }
  * { box-sizing: border-box; margin: 0; padding: 0; }
  html, body { width: 1200px; height: 944px; overflow: hidden; }
  body {
    background: var(--backdrop);
    position: relative;
    font-family: "Open Sans", Arial, sans-serif;
  }
  .card {
    position: absolute;
    width: 640px;
    height: 366px;
    border-radius: 28px;
    overflow: hidden;
    box-shadow: 0 10px 28px rgba(0,0,0,.28);
  }

  /* Front */
  .card-front {
    left: 80px; top: 90px;
    background: radial-gradient(ellipse at 55% 40%, var(--navy-light) 0%, var(--navy) 50%, var(--navy-deep) 100%);
  }
  .brand {
    position: absolute;
    display: flex; align-items: center; gap: 16px;
    font-family: "Ubuntu", sans-serif;
    font-weight: 500;
    color: var(--paper);
    white-space: nowrap;
  }
  .card-front .brand { left: 90px; top: 88px; font-size: 72px; }
  .brand-dot {
    width: 0.62em; height: 0.62em;
    border-radius: 50%;
    background: var(--orange);
    flex: none;
  }
  .front-url {
    position: absolute;
    left: 0; right: 0; top: 252px;
    text-align: center;
    color: var(--paper);
    font-size: 16px;
    letter-spacing: .5px;
  }
  .services-band {
    position: absolute;
    left: 0; right: 0; bottom: 0; height: 68px;
    background: var(--orange);
    color: var(--paper);
    font-size: 17px;
    display: flex; align-items: center; justify-content: center;
    gap: 8px;
  }

  /* Back */
  .card-back { left: 480px; top: 470px; background: var(--paper); }
  .back-art { position: absolute; inset: 0; }
  .card-back .brand {
    left: 60px; top: 30px; font-size: 40px; color: var(--navy);
  }
  .contact-list {
    position: absolute; left: 60px; top: 118px;
    list-style: none;
    color: var(--ink);
    font-size: 16px;
    line-height: 1.35;
  }
  .contact-list li { display: flex; align-items: flex-start; gap: 12px; white-space: nowrap; }
  .contact-list .gap { margin-top: 16px; }
  .contact-list .icon { width: 14px; height: 14px; flex: none; margin-top: 4px; }
  .contact-list .link-accent { color: var(--orange); }
  .icon-square { width: 12px; height: 12px; background: var(--navy); border-radius: 2px; flex: none; margin-top: 5px; margin-left: 1px; margin-right: 1px; }
  .person {
    position: absolute;
    left: 492px; top: 152px;
    color: var(--paper);
    white-space: nowrap;
  }
  .person-name { font-size: 20px; font-weight: 400; }
  .person-title { font-size: 14px; font-style: italic; margin-top: 4px; }
</style>
</head>
<body>

  <section class="card card-front" aria-label="Card front">
    <div class="brand"><span class="brand-dot"></span>Brivatnet</div>
    <p class="front-url">www.brivatnet.example</p>
    <div class="services-band">
      <span>Web Design</span><span>•</span><span>Internet Marketing</span><span>•</span><span>Website Management</span>
    </div>
  </section>

  <section class="card card-back" aria-label="Card back">
    <svg class="back-art" viewBox="0 0 640 366" preserveAspectRatio="none" aria-hidden="true">
      <defs>
        <radialGradient id="panel-blue" cx="70%" cy="50%" r="70%">
          <stop offset="0" stop-color="#2e45b0"/>
          <stop offset="1" stop-color="#141f5e"/>
        </radialGradient>
      </defs>
      <path d="M378 0 C432 80 450 230 412 366 L640 366 L640 0 Z" fill="#f07c1e"/>
      <path d="M402 0 C458 90 472 240 438 366 L640 366 L640 0 Z" fill="#ffffff"/>
      <path d="M410 0 C468 92 482 240 448 366 L640 366 L640 0 Z" fill="url(#panel-blue)"/>
    </svg>

    <div class="brand"><span class="brand-dot"></span>Brivatnet</div>

    <ul class="contact-list">
      <li>
        <svg class="icon" viewBox="0 0 14 14"><path d="M7 1 L13 7 L11 7 L11 13 L3 13 L3 7 L1 7 Z" fill="#1f2f86"/></svg>
        <span>4125 W. Larkspur Ave. Ste. 160<br>Tucson, AZ 85799</span>
      </li>
      <li class="gap">
        <svg class="icon" viewBox="0 0 14 14"><rect x="1" y="3" width="12" height="8" rx="1" fill="#1f2f86"/><path d="M1.5 3.5 L7 8 L12.5 3.5" stroke="#fff" stroke-width="1.2" fill="none"/></svg>
        <span>mark@brivatnet.example</span>
      </li>
      <li>
        <svg class="icon" viewBox="0 0 14 14"><path d="M3 1 L5.5 1 L6.5 4 L5 5.5 C6 7.5 7 8.5 8.5 9 L10 7.5 L13 8.5 L13 11 C13 12 12 13 11 13 C6 13 1 8 1 3 C1 2 2 1 3 1 Z" fill="#1f2f86"/></svg>
        <span>520-318-7051</span>
      </li>
      <li>
        <svg class="icon" viewBox="0 0 14 14"><path d="M3 1 L5.5 1 L6.5 4 L5 5.5 C6 7.5 7 8.5 8.5 9 L10 7.5 L13 8.5 L13 11 C13 12 12 13 11 13 C6 13 1 8 1 3 C1 2 2 1 3 1 Z" fill="#1f2f86"/></svg>
        <span>866-318-7051 (toll free)</span>
      </li>
      <li>
        <span class="icon-square"></span>
        <span>@brivatnet</span>
      </li>
      <li>
        <span class="icon-square"></span>
        <span>www.<span class="link-accent">socialpage.example</span>/brivatnet</span>
      </li>
    </ul>

    <div class="person">
      <p class="person-name">Owen Marsley</p>
      <p class="person-title">President/CEO</p>
    </div>
  </section>

</body>
</html>
```